Design Business Cards for Corventa

We need new businesscards for our company called Corventa. The dimensions is 53mm x 85mm (widht x height), standing, not landscape. We want the businesscards to be creative and original.

On the front side, our company logo, see attached file.
On the backside: a personal photo, name, title, company name, adress, mobile, email and url. Instead of writing ex. "Email", feel free to us a symbol or icon.

Check these three links for inspiration for colours and design;
http://www.brightfold-samples.net/shop/demos/corventa/
http://www.brightfold-samples.net/shop/demos/corventa/activities.html
http://www.brightfold-samples.net/shop/demos/corventa/activity_details.html

```html
<!DOCTYPE html>
<html lang="en">
<head>
<meta charset="utf-8">
<title>Corventa Business Cards</title>
<link rel="stylesheet" href="https://fonts.googleapis.com/css2?family=Montserrat:wght@400;600;700;800&display=swap">
<style>
  :root {
    --bg: #e9ecee;
    --card: #0b0b0c;
    --blue-1: #0a3a6b;
    --blue-2: #0c4a85;
    --blue-3: #0f5799;
    --blue-4: #1466ad;
    --blue-5: #1a74bf;
    --accent: #2f86d6;
    --white: #ffffff;
    --muted: #8a8f96;
    --logo-muted: #6e625d;
    --photo: #bfbfbf;
  }
  * { box-sizing: border-box; margin: 0; padding: 0; }
  html, body { width: 1200px; height: 900px; overflow: hidden; }
  body {
    background: var(--bg);
    font-family: "Montserrat", sans-serif;
    display: flex;
    align-items: center;
    justify-content: center;
    gap: 100px;
  }
  .card {
    position: relative;
    width: 380px;
    height: 609px;
    background: var(--card);
    overflow: hidden;
  }

  /* Front */
  .front-stripes { position: absolute; left: 0; top: 196px; }
  .front-brand {
    position: absolute;
    left: 0;
    right: 34px;
    top: 228px;
    text-align: right;
    color: var(--white);
    font-weight: 800;
    font-size: 40px;
    letter-spacing: 1px;
    display: flex;
    justify-content: flex-end;
    align-items: center;
    gap: 12px;
  }
  .front-brand .dot { width: 14px; height: 14px; border-radius: 50%; background: var(--white); }

  /* Back */
  .photo {
    position: absolute;
    top: 38px;
    right: 40px;
    width: 150px;
    height: 150px;
    border-radius: 50%;
    background: radial-gradient(circle at 50% 40%, #d2d2d2, #a9a9a9);
    border: 4px solid var(--accent);
  }
  .identity {
    position: absolute;
    top: 200px;
    right: 40px;
    text-align: right;
  }
  .identity .name {
    color: var(--accent);
    font-weight: 700;
    font-size: 22px;
    letter-spacing: 1px;
  }
  .identity .title {
    color: var(--muted);
    font-size: 9px;
    letter-spacing: 2px;
    margin-top: 3px;
  }
  .contact {
    position: absolute;
    left: 0;
    top: 262px;
    width: 100%;
    list-style: none;
  }
  .contact li {
    display: flex;
    align-items: center;
    gap: 16px;
    height: 58px;
    padding-left: 30px;
    color: var(--white);
    font-size: 11px;
    line-height: 1.45;
  }
  .contact li:nth-child(1) { background: var(--blue-1); width: 100%; }
  .contact li:nth-child(2) { background: var(--blue-2); width: 92%; }
  .contact li:nth-child(3) { background: var(--blue-3); width: 84%; }
  .contact li:nth-child(4) { background: var(--blue-4); width: 76%; height: 40px; }
  .contact li:nth-child(5) { background: var(--blue-5); width: 68%; height: 28px; }
  .contact svg { flex: none; }
  .back-brand {
    position: absolute;
    left: 34px;
    bottom: 40px;
    color: var(--logo-muted);
    font-weight: 800;
    font-size: 26px;
    letter-spacing: 1px;
  }
</style>
</head>
<body>

  <section class="card card-front" aria-label="Card front">
    <svg class="front-stripes" width="230" height="70" viewBox="0 0 230 70" aria-hidden="true">
      <polygon points="0,8 168,8 186,26 0,26" fill="var(--blue-3)"/>
      <polygon points="0,34 198,34 216,52 0,52" fill="var(--blue-4)"/>
      <polygon points="150,8 168,8 186,26 168,26" fill="var(--accent)"/>
      <polygon points="180,34 198,34 216,52 198,52" fill="var(--accent)"/>
    </svg>
    <div class="front-brand"><span class="dot"></span>CORVENTA</div>
  </section>

  <section class="card card-back" aria-label="Card back">
    <div class="photo" role="img" aria-label="Personal portrait photo"></div>
    <div class="identity">
      <p class="name">YOUR NAME</p>
      <p class="title">TITLE GOES HERE</p>
    </div>
    <ul class="contact">
      <li>
        <svg width="20" height="18" viewBox="0 0 20 18" aria-hidden="true">
          <polygon points="10,1 19,9 16,9 16,17 12,17 12,12 8,12 8,17 4,17 4,9 1,9" fill="var(--white)"/>
        </svg>
        <span>14 Marlow street lake harbour on k3b 2r8<br>ECRA/ESA 4820193</span>
      </li>
      <li>
        <svg width="20" height="18" viewBox="0 0 20 18" aria-hidden="true">
          <path d="M2 5 Q10 0 18 5 L16 8 L13 6 L7 6 L4 8 Z" fill="var(--white)"/>
          <rect x="4" y="9" width="12" height="8" rx="1.5" fill="var(--white)"/>
          <circle cx="10" cy="13" r="2" fill="var(--blue-2)"/>
        </svg>
        <span>000 000 000</span>
      </li>
      <li>
        <svg width="20" height="16" viewBox="0 0 20 16" aria-hidden="true">
          <rect x="1" y="1" width="18" height="14" fill="none" stroke="var(--white)" stroke-width="1.8"/>
          <polyline points="1,1 10,9 19,1" fill="none" stroke="var(--white)" stroke-width="1.8"/>
        </svg>
        <span>Email : info@brightwaveoutdoors.com</span>
      </li>
      <li></li>
      <li></li>
    </ul>
    <div class="back-brand">CORVENTA</div>
  </section>

</body>
</html>
```